Web Dashboard for manufacturing data

We need a dashboard for website to show statistical information on buttons/cards/tiles. There will be 12 buttons on the screen (laptop, tablet) On these buttons there are several key pieces of information on each button. 1) Largest info is % 0-100%. 2) 4 status colours neutral, green, yellow, red. 3) Title- up to 20 characters 4) target here is an example... target=above 90%.- When these buttons are tapped, they take user to more info for that specific data.
1 page

```html
<!DOCTYPE html>
<html lang="en">
<head>
<meta charset="UTF-8">
<title>Manufacturing Dashboard</title>
<link href="https://fonts.googleapis.com/css2?family=Montserrat:wght@500;600&display=swap" rel="stylesheet">
<style>
  :root {
    --green: #17b03b;
    --green-text: #18a93a;
    --yellow: #d6b427;
    --yellow-text: #c9a82a;
    --red: #c41f33;
    --red-text: #c41f33;
    --neutral: #9e918b;
    --neutral-text: #958882;
    --white: #ffffff;
    --page: #ffffff;
  }
  * { box-sizing: border-box; margin: 0; padding: 0; }
  html, body {
    width: 1200px;
    height: 675px;
    overflow: hidden;
    background: var(--page);
    font-family: "Montserrat", Arial, sans-serif;
  }
  .dashboard {
    position: relative;
    width: 1200px;
    height: 675px;
    display: grid;
    grid-template-columns: repeat(4, 283px);
    grid-template-rows: repeat(3, 146px);
    column-gap: 11px;
    row-gap: 72px;
    padding: 71px 0 0 18px;
  }
  .tile {
    position: relative;
    display: block;
    border-radius: 6px;
    background: var(--tile);
    color: var(--white);
    text-decoration: none;
    text-align: center;
  }
  .tile::before {
    content: "";
    position: absolute;
    left: 50%;
    top: 0;
    width: 116px;
    height: 116px;
    margin: -58px 0 0 -58px;
    border-radius: 50%;
    background: var(--tile);
  }
  .tile-value {
    position: absolute;
    left: 50%;
    top: 0;
    width: 96px;
    height: 96px;
    margin: -48px 0 0 -48px;
    border-radius: 50%;
    background: var(--white);
    color: var(--tile-text);
    font-size: 32px;
    font-weight: 500;
    line-height: 96px;
    letter-spacing: 0.5px;
  }
  .tile-title {
    position: absolute;
    left: 0;
    right: 0;
    top: 70px;
    font-size: 15px;
    font-weight: 600;
    letter-spacing: 0.2px;
    text-transform: uppercase;
    white-space: nowrap;
  }
  .tile-target {
    position: absolute;
    left: 0;
    right: 0;
    top: 104px;
    font-size: 13.5px;
    font-weight: 600;
  }
  .status-green { --tile: var(--green); --tile-text: var(--green-text); }
  .status-yellow { --tile: var(--yellow); --tile-text: var(--yellow-text); }
  .status-red { --tile: var(--red); --tile-text: var(--red-text); }
  .status-neutral { --tile: var(--neutral); --tile-text: var(--neutral-text); }
</style>
</head>
<body>
<main class="dashboard">
  <a class="tile status-green" href="#"><span class="tile-value">80%</span><span class="tile-title">Lorem ipsum is simply dummy</span><span class="tile-target">Target=Above 90%</span></a>
  <a class="tile status-yellow" href="#"><span class="tile-value">90%</span><span class="tile-title">Lorem ipsum is simply dummy</span><span class="tile-target">Target=Above 90%</span></a>
  <a class="tile status-red" href="#"><span class="tile-value">91%</span><span class="tile-title">Lorem ipsum is simply dummy</span><span class="tile-target">Target=Above 90%</span></a>
  <a class="tile status-neutral" href="#"><span class="tile-value">80%</span><span class="tile-title">Lorem ipsum is simply dummy</span><span class="tile-target">Target=Above 90%</span></a>

  <a class="tile status-red" href="#"><span class="tile-value">90%</span><span class="tile-title">Lorem ipsum is simply dummy</span><span class="tile-target">Target=Above 90%</span></a>
  <a class="tile status-neutral" href="#"><span class="tile-value">86%</span><span class="tile-title">Lorem ipsum is simply dummy</span><span class="tile-target">Target=Above 90%</span></a>
  <a class="tile status-green" href="#"><span class="tile-value">80%</span><span class="tile-title">Lorem ipsum is simply dummy</span><span class="tile-target">Target=Above 90%</span></a>
  <a class="tile status-yellow" href="#"><span class="tile-value">80%</span><span class="tile-title">Lorem ipsum is simply dummy</span><span class="tile-target">Target=Above 90%</span></a>

  <a class="tile status-neutral" href="#"><span class="tile-value">89%</span><span class="tile-title">Lorem ipsum is simply dummy</span><span class="tile-target">Target=Above 90%</span></a>
  <a class="tile status-yellow" href="#"><span class="tile-value">80%</span><span class="tile-title">Lorem ipsum is simply dummy</span><span class="tile-target">Target=Above 90%</span></a>
  <a class="tile status-red" href="#"><span class="tile-value">70%</span><span class="tile-title">Lorem ipsum is simply dummy</span><span class="tile-target">Target=Above 90%</span></a>
  <a class="tile status-green" href="#"><span class="tile-value">88%</span><span class="tile-title">Lorem ipsum is simply dummy</span><span class="tile-target">Target=Above 90%</span></a>
</main>
</body>
</html>
```